Quenderil - Still Grace Cosmetics

Please design a logo and business cards for new food supplements, cosmetics and herbal fixatives. The products are produced ecologically and biologically in the South Tyrol and Trentino alps. The products are pure and noble. Quenderil = pure vitality Colors Background: dark or black matt (soft touch) Logodesign: powerful, elegant, violet with glossy foil The logo and design should convey warmth, passion and the 6th sense, you should get the impression that you can smell the herbal odor , Logo and business cards for new food supplements, cosmetics and herbal fixatives. The products are produced ecologically and biologically in the South Tyrol and Trentino alps. The products are pure and noble. Quenderil = pure vitality Colors Background: dark or black matt (softtouch) Logodesign: powerful elegant violet with glossy foil The logo and design is meant to convey warmth, passion and the 6th sense, you should get the impression that you can smell the herbal perfume.

Target Market(s)

Food, food supplements, vitality, health

Contact Information for Business Card

Please provide an elegant darf design that is puristic, but has a very good logo design
Elegantes dunkles design, puristisch

Logo Text

Quenderil - still Grace

Colors
6b449b

Requirements
Must have
• SVG Files Alpha channel for foil embossing High-quality design
Nice to have
• Pure elegance
Should not have
• to colorful colors

```html
<!DOCTYPE html>
<html lang="en">
<head>
<meta charset="utf-8">
<title>Quenderil — Business Cards</title>
<link rel="stylesheet" href="https://fonts.googleapis.com/css2?family=Montserrat:wght@400;500;600&display=swap">
<style>
  :root {
    --backdrop: #2b2420;
    --card: #0e0e0f;
    --card-edge: #1a1a1b;
    --violet: #8466bd;
    --violet-deep: #6b449b;
    --ink-light: #f2f2f2;
    --ink-soft: #c9c9cc;
    --emboss: #1d1d1f;
  }
  * { margin: 0; padding: 0; box-sizing: border-box; }
  html, body { width: 1200px; height: 780px; overflow: hidden; }
  body {
    background: var(--backdrop);
    font-family: "Montserrat", Arial, sans-serif;
    position: relative;
  }
  .card {
    position: absolute;
    top: 240px;
    width: 525px;
    height: 300px;
    background: var(--card);
    border: 1px solid var(--card-edge);
    border-radius: 22px;
  }
  .card--front { left: 50px; }
  .card--back { left: 625px; }

  .brand {
    position: absolute;
    top: 52px;
    right: 48px;
    display: flex;
    align-items: center;
    gap: 10px;
  }
  .brand__dot {
    width: 14px;
    height: 14px;
    border-radius: 50%;
    background: var(--violet);
  }
  .brand__name {
    font-size: 40px;
    font-weight: 500;
    color: var(--violet);
    letter-spacing: 0.5px;
  }

  .holder {
    position: absolute;
    left: 48px;
    top: 134px;
  }
  .holder__name {
    font-size: 17px;
    font-weight: 600;
    color: var(--ink-light);
    letter-spacing: 0.6px;
  }
  .holder__role {
    font-size: 11px;
    font-weight: 400;
    color: var(--ink-soft);
    margin-top: 2px;
    letter-spacing: 0.4px;
  }

  .contacts {
    position: absolute;
    left: 48px;
    bottom: 32px;
    list-style: none;
  }
  .contacts__item {
    display: flex;
    align-items: center;
    gap: 9px;
    font-size: 13px;
    color: var(--ink-light);
    line-height: 22px;
    letter-spacing: 0.3px;
  }
  .contacts__badge {
    width: 15px;
    height: 15px;
    border-radius: 50%;
    background: var(--violet-deep);
    color: var(--ink-light);
    font-size: 8px;
    font-weight: 600;
    display: flex;
    align-items: center;
    justify-content: center;
  }

  .card--back .brand {
    top: 50%;
    left: 50%;
    right: auto;
    transform: translate(-50%, -50%);
  }
  .card--back .brand__name {
    color: var(--emboss);
    font-size: 46px;
  }
</style>
</head>
<body>
  <section class="card card--front">
    <div class="brand">
      <span class="brand__dot"></span>
      <span class="brand__name">Quenderil</span>
    </div>
    <div class="holder">
      <p class="holder__name">Lena Marwick</p>
      <p class="holder__role">Managing Director</p>
    </div>
    <ul class="contacts">
      <li class="contacts__item"><span class="contacts__badge">P</span>0482.517.906</li>
      <li class="contacts__item"><span class="contacts__badge">E</span>hello@quenderilcare.com.au</li>
      <li class="contacts__item"><span class="contacts__badge">W</span>quenderilcare.com.au</li>
    </ul>
  </section>

  <section class="card card--back">
    <div class="brand">
      <span class="brand__name">Quenderil</span>
    </div>
  </section>
</body>
</html>
```